Restaurant menu design

Design fine dinning menu for Indian restaurant. Restaurant location is on river side. So if design has some touch of Yarra river of Melbourne and Indian touch. It is not compulsory. Creative and modern design is required.
I want to print in A3 and folded take away sizes so design should for both.
1. In A3, backside we need to design drink menu. I am attaching our current restaurant menu for drinks name and price.

Target Market(s)

Indian / Australian Customer

Industry/Entity Type

Indian Food, Indian fine dining

Colors
F0912C
F2A743
F7CA91
FBE8D2
FDF5EE

Requirements
Must have
• Simple but district design
Should not have
• common other restaurant type menu. Too many colours.

```html
<!DOCTYPE html>
<html lang="en">
<head>
<meta charset="utf-8">
<title>Tara's Table — Menu</title>
<link href="https://fonts.googleapis.com/css2?family=Oswald:wght@500;700&family=Montserrat:wght@400;600;700;800&display=swap" rel="stylesheet">
<style>
:root{
  --bg:#c9c9c9;
  --ink:#141414;
  --panel-dark:#1b1b1b;
  --paper:#ffffff;
  --gold:#c79a5a;
  --gold-deep:#b88a48;
  --gold-text:#e0a64e;
  --muted-light:#d8d8d8;
  --muted-dark:#4a3a24;
}
*{margin:0;padding:0;box-sizing:border-box}
html,body{width:1200px;height:1200px;overflow:hidden;background:var(--bg)}
body{font-family:'Montserrat',sans-serif;position:relative}
.menu{position:absolute;left:20px;top:190px;width:1160px;height:820px;background:var(--panel-dark);overflow:hidden;box-shadow:0 14px 30px rgba(0,0,0,.25)}
.dark-food{position:absolute;left:380px;top:330px;width:520px;height:290px;background:radial-gradient(ellipse at 60% 60%,#3a2d22 0%,#1b1b1b 70%)}
.cover{position:absolute;left:28px;top:28px;width:340px;height:600px;background:var(--paper);border:3px solid var(--gold);outline:1px solid var(--gold);outline-offset:-9px;text-align:center;z-index:3}
.brand{margin-top:38px;font-family:'Oswald',sans-serif;font-weight:700;font-size:40px;color:var(--ink);letter-spacing:.5px}
.brand-rule{width:150px;height:2px;background:var(--ink);margin:6px auto 22px}
.cover-kicker{font-family:'Oswald',sans-serif;font-weight:700;font-size:24px;color:var(--ink);letter-spacing:1px}
.cover-title{font-family:'Montserrat',sans-serif;font-weight:800;font-size:88px;line-height:1;color:var(--gold)}
.ribbon{margin:6px auto 0;width:322px;background:var(--gold);color:#fff;font-size:10.5px;font-weight:700;padding:5px 0}
.cover-photo{width:270px;height:170px;margin:34px auto 0;border-radius:50%;background:radial-gradient(ellipse,#d49a5a 0%,#e9e2d8 45%,#f4f4f4 70%)}

.item{position:relative;margin-bottom:14px}
.item-name{font-size:10px;font-weight:700;color:var(--gold-text);padding-right:46px}
.item-desc{font-size:9px;line-height:1.35;color:var(--muted-light)}
.price{position:absolute;right:0;top:-2px;font-size:14px;color:var(--gold-text)}
.section-title{font-family:'Oswald',sans-serif;font-weight:700;font-size:20px;color:#fff;margin-bottom:12px}

.band{position:absolute;left:0;top:620px;width:880px;height:200px;background:var(--gold)}
.band-title{position:absolute;left:40px;top:34px;font-family:'Oswald',sans-serif;font-weight:700;font-size:24px;color:#fff;white-space:nowrap}
.samosa{position:absolute;left:20px;top:86px;width:180px;height:140px;border-radius:50%;background:radial-gradient(circle,#d9a24c 0%,#e8c895 45%,#f3efe8 70%)}
.band .col{position:absolute}
.band .item{margin-bottom:12px}
.band .item-name{color:#fff}
.band .item-desc{color:var(--muted-dark)}
.band .price{color:#fff}
.col-a{left:252px;top:40px;width:236px}
.col-b{left:512px;top:18px;width:240px}
.col-c{left:772px;top:10px;width:100px}
.col-c .price{position:static;display:block;text-align:right;margin-bottom:2px}
.col-c .item-name{padding-right:0}

.tandoori{position:absolute;left:420px;top:16px;width:200px;height:120px;border-radius:50%;background:radial-gradient(ellipse,#c8651f 0%,#7a4320 55%,#1b1b1b 75%)}
.dip{position:absolute;left:400px;top:110px;width:60px;height:50px;border-radius:50%;background:radial-gradient(circle,#cfe0a0 0%,#a88a4a 55%,#1b1b1b 75%)}
.nonveg{position:absolute;left:410px;top:180px;width:240px;z-index:2}
.chaat{position:absolute;left:670px;top:30px;width:200px;z-index:2}
.indo{position:absolute;left:670px;top:260px;width:200px;z-index:2}
.indo .price small{display:block;font-size:12px;text-align:right}
.item-multi .item-name{padding-right:76px}
.item-multi .item-desc{padding-right:0;margin-top:14px}

.side{position:absolute;left:900px;top:0;width:260px;height:820px;background:var(--paper);padding:30px 22px 0 24px}
.side .section-title{color:var(--ink);font-size:19px;line-height:1.1}
.side .item-name{color:var(--gold-deep);padding-right:0}
.side .item-desc{color:#333}
.side .price{color:var(--gold-deep)}
.side .item{width:150px;position:static;margin-bottom:10px}
.side .row{position:relative}
.side .row .price{top:0;right:0}
.curry{position:absolute;right:-30px;top:200px;width:100px;height:110px;border-radius:50%;background:radial-gradient(ellipse,#d9772a 0%,#e5b47c 50%,#fff 72%)}
.special{margin-top:14px;width:216px}
.soup{position:absolute;left:40px;top:665px;width:190px;height:130px;border-radius:50%;background:radial-gradient(ellipse,#e39a2a 0%,#efe3cf 55%,#fff 72%)}
</style>
</head>
<body>
<main class="menu">
  <div class="dark-food" role="img" aria-label="Dark overhead photo of noodles, sauces and bowls"></div>

  <section class="cover">
    <div class="brand">Tara's Table</div>
    <div class="brand-rule"></div>
    <div class="cover-kicker">TARA'S TABLE</div>
    <div class="cover-title">MENU</div>
    <div class="ribbon">Modern &amp; Classic Indian Dining Riverside Quay, Melbourne</div>
    <div class="cover-photo" role="img" aria-label="Grilled stuffed chicken breast with asparagus on a white plate"></div>
  </section>

  <div class="tandoori" role="img" aria-label="Tandoori chicken pieces with onion and lemon on a wooden board"></div>
  <div class="dip" role="img" aria-label="Bowl of mint chutney"></div>

  <section class="nonveg">
    <h2 class="section-title">Non-Vegetarian Entrées</h2>
    <div class="item"><span class="price">$20</span><p class="item-name">Smoke Tandoori Chicken Tikka</p><p class="item-desc">Charcoal-grilled chicken marinated overnight with aromatic spices, finished with a touch of smokey infusion.</p></div>
    <div class="item"><span class="price">$20</span><p class="item-name">Chicken Malai Tikka</p><p class="item-desc">Tender chicken morsels marinated in cream, cheese &amp; cardamom, cooked gently in the tandoor for a melt-in-mouth experience.</p></div>
    <div class="item"><span class="price">$22</span><p class="item-name">Awadhi Fish Tikka</p><p class="item-desc">Fresh barramundi fillets marinated with hand-pounded Awadhi spices, grilled for a delicate smokey finish.</p></div>
    <div class="item"><span class="price">$24</span><p class="item-name">Tandoori Tiger Prawns</p><p class="item-desc">Fresh barramundi fillets marinated with hand-pounded Awadhi spices, grilled for a delicate smokey finish.</p></div>
    <div class="item"><span class="price">$22</span><p class="item-name">Lamb Gilafi Seekh</p><p class="item-desc">Minced lamb spiced with herbs, peppers &amp; aromatics, skewered &amp; flame-roasted, served with minted yogurt.</p></div>
    <div class="item"><span class="price">$39</span><p class="item-name">Tandoori Platter</p><p class="item-desc">A chef's selection of smoky tandoori classics: Chicken Tikka, Malai Tikka, Lamb Seekh &amp; Awadhi Fish, presented with a medley of chutneys &amp; dips.</p></div>
  </section>

  <section class="chaat">
    <h2 class="section-title">Chaat</h2>
    <div class="item"><span class="price">$20</span><p class="item-name">Panipuri Experience</p><p class="item-desc">Charcoal-grilled chicken marinated overnight with aromatic spices, finished with a touch of smokey.</p></div>
    <div class="item"><span class="price">$20</span><p class="item-name">Burrata Chaat</p><p class="item-desc">Charcoal-grilled chicken marinated overnight with aromatic spices, finished with a touch of smokey.</p></div>
    <div class="item"><span class="price">$18</span><p class="item-name">Deconstructed Samosa Chaat</p><p class="item-desc">Crispy samosa pastry crumbles over spiced potato &amp; peas, dressed with chutneys, yogurt &amp; pomegranate jewels.</p></div>
  </section>

  <section class="indo">
    <h2 class="section-title">Indo-Chinese</h2>
    <div class="item"><span class="price">$22</span><p class="item-name">Vegetable Manchurian Dry</p><p class="item-desc">Golden-fried vegetable dumplings wok-tossed in garlic, chilli &amp; soy glaze.</p></div>
    <div class="item"><span class="price">$24</span><p class="item-name">Paneer Chilli Dry</p><p class="item-desc">Cottage cheese cubes tossed with peppers, onions &amp; chilli-garlic soy reduction.</p></div>
    <div class="item"><span class="price">$26</span><p class="item-name">Chilli Chicken Dry</p><p class="item-desc">Cottage cheese cubes tossed with peppers, onions &amp; chilli-garlic soy reduction.</p></div>
    <div class="item item-multi"><span class="price"><small>Veg $22</small><small>Chicken $24</small></span><p class="item-name">Oriental Noodles</p><p class="item-desc">Stir-fried noodles with seasonal vegetables, wok-seared with soy &amp; garlic.</p></div>
  </section>

  <section class="band">
    <h2 class="band-title">Vegetarian Entrées</h2>
    <div class="samosa" role="img" aria-label="Plate of samosas with a small bowl of red sauce"></div>
    <div class="col col-a">
      <div class="item"><span class="price">$16</span><p class="item-name">Classic Samosa</p><p class="item-desc">Handcrafted pastry parcels filled with spiced potatoes &amp; peas, served with a duo of fresh mint-coriander chutney and sweet mango relish.</p></div>
      <div class="item"><span class="price">$16</span><p class="item-name">Crispy Onion &amp; Spinach Bhaji</p><p class="item-desc">Crisp golden fritters of baby spinach &amp; onion, delicately spiced, paired with house chutneys.</p></div>
    </div>
    <div class="col col-b">
      <div class="item"><span class="price">$18</span><p class="item-name">Harabhara Edamame Kebab</p><p class="item-desc">Pan-seared medallions of edamame and garden vegetables, stuffed with soft cheese and herbs, served with tangy yogurt dip.</p></div>
      <div class="item"><span class="price">$22</span><p class="item-name">Zafrani Paneer Tikka</p><p class="item-desc">Cubes of cottage cheese marinated in saffron, cardamom &amp; smoky tandoor spices, grilled to perfection, served with mint chutney and microgreens.</p></div>
    </div>
    <div class="col col-c">
      <div class="item"><span class="price">$16</span><p class="item-name">Vada Pav Sliders</p><p class="item-desc">A gourmet take on Mumbai's street legend: spiced potato croquette in a butter brioche bun, layered with tamarind, mint-coriander chutney &amp; fiery thecha.</p></div>
    </div>
  </section>

  <aside class="side">
    <h2 class="section-title">Classic Curries</h2>
    <div class="row"><span class="price">$20</span><div class="item"><p class="item-name">Paneer / Vegetable</p><p class="item-desc">Choose your protein with a choice of gourmet curry bases.</p></div></div>
    <div class="row"><span class="price">$28</span><div class="item"><p class="item-name">Chicken / Lamb</p><p class="item-desc">Choose your protein with a choice of gourmet curry bases.</p></div></div>
    <div class="row"><span class="price">$30</span><div class="item"><p class="item-name">Prawns / Fish</p><p class="item-desc">Choose your protein with a choice of gourmet curry bases.</p></div></div>
    <div class="item"><p class="item-name">Vindaloo —</p><p class="item-desc">Fiery Goan-style curry with red chillies &amp; vinegar.</p></div>
    <div class="item"><p class="item-name">Korma —</p><p class="item-desc">Mild, creamy cashew &amp; saffron curry.</p></div>
    <div class="item"><p class="item-name">Masala</p><p class="item-desc">Tomato &amp; onion base enriched with cream &amp; butter.</p></div>
    <div class="item"><p class="item-name">Madras</p><p class="item-desc">Coconut-based curry with onions, garlic &amp; curry leaves.</p></div>
    <div class="curry" role="img" aria-label="Bowl of orange curry garnished with coriander"></div>

    <section class="special">
      <h2 class="section-title">Tara's Table Special Vegetarian Curries</h2>
      <div class="row"><span class="price">$26</span><div class="item"><p class="item-name">Sham Savera Kofta</p><p class="item-desc">Spinach dumplings filled with cottage cheese, simmered in a rich tomato-butter sauce — a true royal delicacy.</p></div></div>
      <div class="row"><span class="price">$28</span><div class="item"><p class="item-name">Mexican Salsa Paneer</p><p class="item-desc">Paneer cubes tossed in a fusion of roasted Mexican-style tomato salsa and Indian spices — a bold East-meets-West creation.</p></div></div>
      <div class="row"><span class="price">$28</span><div class="item"><p class="item-name">Mushroom Mutter Masala</p><p class="item-desc">Tender mushrooms and garden peas in a spiced onion-tomato gravy, finished with cream.</p></div></div>
    </section>
    <div class="soup" role="img" aria-label="Kofta dumplings in orange gravy on a white plate"></div>
  </aside>
</main>
</body>
</html>
```